Awesome photographers card for an awesome new business

Double sided business card Black background and silver logo in middle on one side. Details on otherside. please keep it simple

Photographer

Gavin Tolley
0482615073
GavinTolleyPhotography82@lumenpost.com
www.GavinTolleyPhotography.com.au
Instagram _Gavin_tolley

Requirements
Must have
• My logo in Silver
• please use instagram logo instead of "Instagram"

```html
<!DOCTYPE html>
<html lang="en">
<head>
<meta charset="utf-8">
<title>Gavin Tolley Photography – Business Card</title>
<link rel="stylesheet" href="https://fonts.googleapis.com/css2?family=Montserrat:wght@400;500;600&family=Arimo:wght@400&display=swap">
<style>
  :root {
    --backdrop: #2a2a2a;
    --card: #0f0f0f;
    --card-back: #131313;
    --silver: #d6d6d6;
    --white: #ffffff;
    --muted: #9a9a9a;
    --rule: #cfcfcf;
  }
  * { box-sizing: border-box; margin: 0; padding: 0; }
  html, body {
    width: 1200px; height: 1200px; overflow: hidden;
    background: var(--backdrop);
  }
  .canvas {
    width: 1200px; height: 1200px;
    display: flex; flex-direction: column; align-items: center; justify-content: center;
    gap: 60px;
  }
  .card {
    width: 880px; height: 500px;
    background: var(--card);
    box-shadow: 0 14px 40px rgba(0,0,0,.55);
    position: relative;
  }
  .card--back { background: var(--card-back); }

  .brand {
    display: flex; align-items: center; gap: 16px;
    font-family: "Montserrat", sans-serif;
    font-weight: 500;
    color: var(--silver);
    letter-spacing: .12em;
    text-transform: uppercase;
  }
  .brand__dot {
    border: 3px solid var(--silver);
    border-radius: 50%;
    flex: none;
  }
  .card--front .brand {
    position: absolute; left: 50%; top: 50%;
    transform: translate(-50%, -50%);
    font-size: 30px; white-space: nowrap;
  }
  .card--front .brand__dot { width: 40px; height: 40px; }

  .card--back .brand {
    position: absolute; left: 60px; top: 50%;
    transform: translateY(-50%);
    width: 250px;
    font-size: 22px; line-height: 1.35;
  }
  .card--back .brand__dot { width: 32px; height: 32px; }

  .divider {
    position: absolute; left: 340px; top: 120px;
    width: 2px; height: 260px;
    background: var(--rule);
  }
  .details {
    position: absolute; left: 380px; top: 128px;
  }
  .details__name {
    font-family: "Montserrat", sans-serif;
    font-weight: 600; font-size: 30px;
    color: var(--white); letter-spacing: .04em;
    text-transform: uppercase;
  }
  .details__role {
    font-family: "Montserrat", sans-serif;
    font-weight: 400; font-size: 22px;
    color: var(--muted); letter-spacing: .08em;
    text-transform: uppercase;
    margin-top: 2px; margin-bottom: 18px;
  }
  .contact { list-style: none; }
  .contact__item {
    display: flex; align-items: center; gap: 14px;
    font-family: "Arimo", sans-serif;
    font-size: 20px; color: var(--white);
    height: 34px; white-space: nowrap;
  }
  .contact__icon { width: 22px; height: 22px; flex: none; }
</style>
</head>
<body>
<main class="canvas">

  <section class="card card--front" aria-label="Card front">
    <div class="brand">
      <span class="brand__dot"></span>
      <span class="brand__name">Gavin Tolley Photography</span>
    </div>
  </section>

  <section class="card card--back" aria-label="Card back">
    <div class="brand">
      <span class="brand__dot"></span>
      <span class="brand__name">Gavin Tolley Photography</span>
    </div>

    <div class="divider"></div>

    <div class="details">
      <h1 class="details__name">Gavin Tolley</h1>
      <p class="details__role">Photographer</p>
      <ul class="contact">
        <li class="contact__item">
          <svg class="contact__icon" viewBox="0 0 24 24" aria-hidden="true">
            <path d="M3 9c0-3 4-5 9-5s9 2 9 5v2h-5V9H8v2H3z" fill="#e6e6e6"/>
            <rect x="6" y="12" width="12" height="8" rx="1" fill="#e6e6e6"/>
            <circle cx="12" cy="16" r="2" fill="#131313"/>
          </svg>
          <span>0482615073</span>
        </li>
        <li class="contact__item">
          <svg class="contact__icon" viewBox="0 0 24 24" aria-hidden="true">
            <rect x="2" y="5" width="20" height="14" fill="#e6e6e6"/>
            <path d="M2 5l10 8 10-8M2 19l7-7M22 19l-7-7" stroke="#131313" stroke-width="1.5" fill="none"/>
          </svg>
          <span>GavinTolleyPhotography82@lumenpost.com</span>
        </li>
        <li class="contact__item">
          <svg class="contact__icon" viewBox="0 0 24 24" aria-hidden="true" fill="none" stroke="#e6e6e6" stroke-width="1.6">
            <circle cx="12" cy="12" r="10"/>
            <ellipse cx="12" cy="12" rx="4.5" ry="10"/>
            <path d="M2 12h20M4 7h16M4 17h16"/>
          </svg>
          <span>www.GavinTolleyPhotography.com.au</span>
        </li>
        <li class="contact__item">
          <svg class="contact__icon" viewBox="0 0 24 24" aria-hidden="true">
            <rect x="3" y="3" width="18" height="18" rx="3" fill="none" stroke="#e6e6e6" stroke-width="2"/>
          </svg>
          <span>Gavin_tolley</span>
        </li>
      </ul>
    </div>
  </section>

</main>
</body>
</html>
```